Maplewood Farms - business cards
Business Card
Project: Maplewood Farms - business cards
Maplewood Farms - business cards - Agriculture
Creative Brief
Use same font as used in my logo
Glen Patters
38672 Red Falcon Lane Cheney, WA 99004
gpatters@ironvale-partners.example
Can I see the design for a one sided card vs a 2 sided card? I want to send to the printer to see how much more it costs for 2 sided.
we might just do one sided; for a two sided card, just the logo

```html
<!DOCTYPE html>
<html lang="en">
<head>
<meta charset="utf-8">
<title>Maplewood Farms – Stationery</title>
<link href="https://fonts.googleapis.com/css2?family=Open+Sans:wght@400;700&display=swap" rel="stylesheet">
<style>
:root{
  --board:#2b1d17;
  --board-light:#3a2820;
  --paper:#ffffff;
  --paper-shade:#f1f0ee;
  --gold:#e2a524;
  --gold-light:#f2c45a;
  --brown:#7a5427;
  --ink:#6b6b6b;
  --label:#b9aea6;
}
*{margin:0;padding:0;box-sizing:border-box}
html,body{width:1200px;height:444px;overflow:hidden;background:var(--board)}
body{font-family:"Open Sans",Arial,sans-serif}
.board{position:relative;width:1200px;height:444px;
  background:radial-gradient(ellipse at 50% 45%,var(--board-light),var(--board) 70%)}
.piece{position:absolute;background:var(--paper);box-shadow:0 3px 10px rgba(0,0,0,.55);overflow:hidden}
.piece svg.wave{position:absolute;left:0;top:0;width:100%;height:100%}
.label{position:absolute;font-size:6px;color:var(--label);letter-spacing:.2px;white-space:nowrap}
.brand{font-weight:700;color:var(--brown);white-space:nowrap;display:flex;align-items:center;gap:4px;text-transform:uppercase;letter-spacing:.4px;line-height:1}
.brand .dot{display:inline-block;border-radius:50%;background:var(--gold);flex:none}
.contact{color:var(--ink);font-size:4px;line-height:6px;font-weight:400;white-space:nowrap}

/* business cards */
.card{left:19px;width:168px;height:96px}
.card-front{top:128px}
.card-back{top:256px}
.card-front .holder{position:absolute;right:10px;top:8px;text-align:right;font-size:5px;line-height:7px;color:var(--brown);font-weight:700}
.card-front .brand{position:absolute;left:12px;top:46px;font-size:9px}
.card-front .brand .dot{width:8px;height:8px}
.card-back .brand{position:absolute;left:0;right:0;top:34px;justify-content:center;font-size:12px}
.card-back .brand .dot{width:10px;height:10px}

/* letterheads */
.letterhead{top:19px;width:276px;height:384px}
.letterhead-first{left:210px}
.letterhead-second{left:505px}
.letterhead .brand{position:absolute;top:16px;font-size:9px}
.letterhead .brand .dot{width:8px;height:8px}
.letterhead-first .brand{left:58px}
.letterhead-second .brand{left:0;right:0;justify-content:center}
.letterhead .contact{position:absolute;left:184px;top:12px;font-size:3.6px;line-height:5px}
.letterhead .footer{position:absolute;left:0;right:0;bottom:8px;text-align:center;font-size:4px;color:var(--paper)}

/* envelopes */
.envelope{left:826px;width:250px;height:96px}
.env-back-light{top:53px}
.env-back-gold{top:118px;background:var(--gold)}
.env-back-plain{top:200px}
.env-front{top:290px;height:112px}
.envelope .brand{position:absolute;font-size:7px}
.envelope .brand .dot{width:6px;height:6px}
.env-back-light .brand{left:150px;top:20px}
.env-back-gold .brand{left:150px;top:20px;color:var(--paper)}
.env-back-gold .brand .dot{background:var(--paper)}
.env-back-plain .brand{left:150px;top:20px}
.env-front .brand{left:12px;top:12px}
.env-front .contact{position:absolute;left:14px;top:24px;font-size:3.6px;line-height:5px}
</style>
</head>
<body>
<main class="board">

  <section class="piece card card-front">
    <svg class="wave" viewBox="0 0 168 96" preserveAspectRatio="none">
      <path d="M0 80 Q84 92 168 70 L168 96 L0 96 Z" fill="var(--gold)"/>
      <path d="M0 77 Q84 88 168 67" fill="none" stroke="var(--paper-shade)" stroke-width="2"/>
    </svg>
    <div class="holder">Glen Patters
      <div class="contact">38672 Red Falcon Lane<br>Cheney, WA 99004<br>(509) 555-0142<br>gpatters@ironvale-partners.example</div>
    </div>
    <div class="brand"><span class="dot"></span>Maplewood Farms</div>
  </section>
  <div class="label" style="left:21px;top:230px">Front Card</div>

  <section class="piece card card-back">
    <svg class="wave" viewBox="0 0 168 96" preserveAspectRatio="none">
      <path d="M0 80 Q84 94 168 76 L168 96 L0 96 Z" fill="var(--gold)"/>
    </svg>
    <div class="brand"><span class="dot"></span>Maplewood Farms</div>
  </section>
  <div class="label" style="left:21px;top:358px">Back Card</div>

  <section class="piece letterhead letterhead-first">
    <svg class="wave" viewBox="0 0 276 384" preserveAspectRatio="none">
      <path d="M0 318 Q130 370 276 300 L276 384 L0 384 Z" fill="var(--gold)"/>
      <path d="M0 313 Q130 363 276 294" fill="none" stroke="var(--paper-shade)" stroke-width="3"/>
    </svg>
    <div class="brand"><span class="dot"></span>Maplewood Farms</div>
    <div class="contact">38672 Red Falcon Lane<br>Cheney, WA 99004<br>(509) 555-0142<br>gpatters@ironvale-partners.example</div>
    <div class="footer">maplewoodfarms.example</div>
  </section>
  <div class="label" style="left:316px;top:410px">Letterhead Page 1</div>

  <section class="piece letterhead letterhead-second">
    <svg class="wave" viewBox="0 0 276 384" preserveAspectRatio="none">
      <path d="M0 318 Q130 370 276 300 L276 384 L0 384 Z" fill="var(--gold)"/>
      <path d="M0 313 Q130 363 276 294" fill="none" stroke="var(--paper-shade)" stroke-width="3"/>
    </svg>
    <div class="brand"><span class="dot"></span>Maplewood Farms</div>
  </section>
  <div class="label" style="left:611px;top:410px">Letterhead Page 2</div>

  <section class="piece envelope env-back-light">
    <svg class="wave" viewBox="0 0 250 96" preserveAspectRatio="none">
      <path d="M0 80 Q125 96 250 72 L250 96 L0 96 Z" fill="var(--gold)"/>
    </svg>
    <div class="brand"><span class="dot"></span>Maplewood Farms</div>
  </section>
  <section class="piece envelope env-back-gold">
    <svg class="wave" viewBox="0 0 250 96" preserveAspectRatio="none">
      <path d="M0 60 Q125 40 250 56" fill="none" stroke="var(--gold-light)" stroke-width="1.5"/>
    </svg>
    <div class="brand"><span class="dot"></span>Maplewood Farms</div>
  </section>
  <section class="piece envelope env-back-plain">
    <svg class="wave" viewBox="0 0 250 96" preserveAspectRatio="none">
      <path d="M0 0 L125 48 L250 0" fill="var(--paper-shade)" stroke="#dddddd" stroke-width="1"/>
    </svg>
    <div class="brand"><span class="dot"></span>Maplewood Farms</div>
  </section>
  <section class="piece envelope env-front">
    <svg class="wave" viewBox="0 0 250 112" preserveAspectRatio="none">
      <path d="M0 92 Q125 108 250 84 L250 112 L0 112 Z" fill="var(--gold)"/>
    </svg>
    <div class="brand"><span class="dot"></span>Maplewood Farms</div>
    <div class="contact">38672 Red Falcon Lane<br>Cheney, WA 99004</div>
  </section>
  <div class="label" style="left:916px;top:410px">Envelope Front &amp; Back</div>

</main>
</body>
</html>
```